Swimming Pool Supply Company Business Cards

We need business cards designed for company. These need to be easy to edit so that we can fill in names, titles, and contact info for each person who works here.

Dalton R. Whitfield
Manager of Legal & Finance
K.L. Brisbane, Incorporated

4837 Grenway Avenue
Marlow Heights, PA 19243

E. dalton@klbrisbane-example.com
M. (215) 555-0173
O. (215) 555-0148

Contact Information for Business Card

Looking to upgrade current business cards with graphic that can be edited. Looking for fresh ideas for an age old industry.

Font styles to use
Serif
Sans Serif

Colors

Designer to choose colors to be used in the design.

Requirements
Must have
• Professional, fresh, unique but professional

```html
<!DOCTYPE html>
<html lang="en">
<head>
<meta charset="utf-8">
<title>K.L. Brisbane Business Cards</title>
<link href="https://fonts.googleapis.com/css2?family=Arimo:wght@400;700&display=swap" rel="stylesheet">
<style>
  :root {
    --bg: #e9ebee;
    --card: #f7f7f5;
    --card-white: #ffffff;
    --ink: #141414;
    --blue: #1f67c1;
    --blue-pale: #d9e2ef;
    --pattern: #eef1f5;
  }
  * { box-sizing: border-box; margin: 0; padding: 0; }
  html, body {
    width: 1200px; height: 1200px; overflow: hidden;
    background: var(--bg);
    font-family: "Arimo", Arial, sans-serif;
  }
  .sheet {
    width: 1200px; height: 1200px;
    display: flex; flex-direction: column; align-items: center; justify-content: center;
    gap: 52px;
  }
  .card {
    position: relative; width: 900px; height: 514px; overflow: hidden;
    box-shadow: 0 6px 18px rgba(0,0,0,.14);
  }
  /* Contact side */
  .card--contact { background: var(--card); }
  .card__watermark {
    position: absolute; left: 40px; bottom: 30px;
    font-weight: 700; font-size: 88px; letter-spacing: -1px;
    color: var(--blue-pale); line-height: 1; white-space: nowrap;
  }
  .contact { position: absolute; left: 70px; top: 44px; color: var(--ink); }
  .contact__name {
    font-weight: 700; font-size: 62px; letter-spacing: -0.5px; line-height: 1;
    padding-bottom: 8px; border-bottom: 4px solid var(--ink); width: 740px;
  }
  .contact__title { font-size: 19px; margin-top: 6px; }
  .contact__address, .contact__lines { font-size: 32px; line-height: 1.2; }
  .contact__address { margin-top: 20px; font-weight: 700; }
  .contact__lines { margin-top: 8px; font-weight: 400; }
  .card__brand {
    position: absolute; right: 60px; bottom: 40px;
    font-weight: 700; font-size: 54px; color: var(--blue); line-height: 1;
  }
  /* Brand side */
  .card--brand { background: var(--card-white); }
  .card__pattern { position: absolute; inset: 0; background: var(--pattern); opacity: .6; }
  .card__waves { position: absolute; inset: 0; }
  .brand {
    position: absolute; right: 50px; top: 120px; text-align: right; color: var(--blue);
  }
  .brand__name { font-weight: 700; font-size: 120px; line-height: 1; letter-spacing: -1px; white-space: nowrap; }
  .brand__tagline { font-weight: 700; font-size: 24px; margin-top: 14px; letter-spacing: .5px; white-space: nowrap; }
</style>
</head>
<body>
<main class="sheet">
  <section class="card card--contact">
    <div class="card__watermark" aria-hidden="true">BRISBANE</div>
    <div class="contact">
      <h1 class="contact__name">Dalton R. Whitfield</h1>
      <p class="contact__title">Manager of Legal &amp; Finance K.L. Brisbane, Incorporated</p>
      <p class="contact__address">4837 Grenway Avenue<br>Marlow Heights, PA 19243</p>
      <p class="contact__lines">E. dalton@klbrisbane-example.com<br>M. (215) 555-0173<br>O. (215) 555-0148</p>
    </div>
    <div class="card__brand">BRISBANE</div>
  </section>

  <section class="card card--brand">
    <div class="card__pattern" role="img" aria-label="Faint repeating brand-name background texture"></div>
    <svg class="card__waves" viewBox="0 0 900 514" aria-hidden="true">
      <path d="M40 0 C 80 150, 110 330, 240 400 S 600 460, 900 450" fill="none" stroke="var(--blue)" stroke-width="9"/>
      <path d="M70 0 C 110 140, 140 310, 270 380 S 620 430, 900 420" fill="none" stroke="var(--blue)" stroke-width="3"/>
    </svg>
    <div class="brand">
      <div class="brand__name">BRISBANE</div>
      <div class="brand__tagline">SWIMMING POOLS, SUPPLIES &amp; ACCESSORIES</div>
    </div>
  </section>
</main>
</body>
</html>
```